New business card design to go with our new logo

just want an eye-catching business card to go with our new logo. We are open to double sided or single sided. Just want it to have the following info on it. Whatever layout you think looks best.

First and Last Name
Title
Phone 801-555-0187
Address 312 W. Larkmoor Avenue Orem UT 84057
Email thecrew@meadowstailandkennel.example

Industry/Entity Type

Business

```html
<!DOCTYPE html>
<html lang="en">
<head>
<meta charset="utf-8">
<title>Meadow's Tail &amp; Kennel – Business Card</title>
<link href="https://fonts.googleapis.com/css2?family=Roboto:wght@400;500;700&family=Roboto+Condensed:wght@700&display=swap" rel="stylesheet">
<style>
  :root {
    --backdrop: #2b2b2b;
    --sky: #2fa7d9;
    --tangerine: #f78f4e;
    --paper: #f2f2f2;
    --white: #ffffff;
  }
  * { margin: 0; padding: 0; box-sizing: border-box; }
  html, body {
    width: 1200px; height: 960px; overflow: hidden;
    background: var(--backdrop);
    font-family: "Roboto", Arial, sans-serif;
  }
  .card {
    position: absolute;
    width: 600px; height: 343px;
    border-radius: 22px;
    overflow: hidden;
  }
  .card--front { left: 314px; top: 113px; background: var(--sky); }
  .card--back  { left: 311px; top: 472px; background: var(--tangerine); }

  .card__swoosh { position: absolute; inset: 0; width: 600px; height: 343px; }

  .contact { position: absolute; left: 24px; top: 86px; color: var(--white); }
  .contact__name {
    font-family: "Roboto Condensed", Arial, sans-serif;
    font-weight: 700; font-size: 22px; color: var(--tangerine);
    line-height: 26px;
  }
  .contact__title { font-size: 15px; font-weight: 500; line-height: 20px; }
  .contact__block { font-size: 14px; line-height: 19px; }
  .contact__address { margin-top: 20px; }
  .contact__reach { margin-top: 8px; }
  .contact__email { letter-spacing: -0.35px; }

  .brand {
    position: absolute;
    display: flex; flex-direction: column; align-items: center;
  }
  .card--front .brand { left: 345px; top: 82px; width: 230px; }
  .card--back .brand { left: 0; top: 84px; width: 600px; }
  .brand__dot {
    width: 72px; height: 72px; border-radius: 50%;
    background: var(--tangerine);
    margin-bottom: 18px;
  }
  .card--back .brand__dot { background: var(--white); width: 80px; height: 80px; }
  .brand__name {
    font-family: "Roboto", Arial, sans-serif;
    font-weight: 700; font-size: 21px; color: var(--sky);
    white-space: nowrap;
  }
  .card--back .brand__name { color: var(--white); font-size: 24px; }

  .back__url {
    position: absolute; left: 0; width: 600px; top: 294px;
    text-align: center; color: var(--white);
    font-size: 13px; letter-spacing: 2.6px;
  }
</style>
</head>
<body>
  <section class="card card--front">
    <svg class="card__swoosh" viewBox="0 0 600 343" aria-hidden="true">
      <path d="M316,0 C262,85 262,215 318,264 C368,306 425,330 452,343 L600,343 L600,0 Z" fill="var(--tangerine)"/>
      <path d="M316,0 C272,80 272,210 332,260 C378,300 438,326 472,343 L600,343 L600,0 Z" fill="var(--paper)"/>
    </svg>
    <div class="contact">
      <div class="contact__name">JOHN SMITH</div>
      <div class="contact__title">CEO/FOUNDER</div>
      <div class="contact__block contact__address">
        312 W. Larkmoor Avenue<br>Orem UT 84057
      </div>
      <div class="contact__block contact__reach">
        P : 801-555-0187<br>
        <span class="contact__email">thecrew@meadowstailandkennel.example</span><br>
        meadowstailandkennel.example
      </div>
    </div>
    <div class="brand">
      <div class="brand__dot"></div>
      <div class="brand__name">Meadow's Tail &amp; Kennel</div>
    </div>
  </section>

  <section class="card card--back">
    <div class="brand">
      <div class="brand__dot"></div>
      <div class="brand__name">Meadow's Tail &amp; Kennel</div>
    </div>
    <div class="back__url">www.meadowstailandkennel.example</div>
  </section>
</body>
</html>
```